Business Card Design

This is a new business to be run from my home. I have attended certificate workshops run by Dr Derek Onwu who is a Master Trainer in Harbor Steps Method.
I wish to communicate to people that Tai Chi is for everyone, no matter their age, gender or fitness levels. Tai Chi is taught both standing & seated.
The card should have a slightly Asian feel, mainly printed in black & white with perhaps a little soft pink &/or green.

Target Market(s)

people of all ages from 10 years up, poor fitness & mild disabilities.

Industry/Entity Type

Fitness

Contact Information for Business Card

Wexmoor Tai Chi for Fitness, Health & Relaxation

Branna Holt, Certificated Leader

ph 4091 5528

Requirements
Nice to have
• a feeling of health & peace.
Should not have
• bright colours, fancy fonts

```html
<!DOCTYPE html>
<html lang="en">
<head>
<meta charset="UTF-8">
<title>Wexmoor Tai Chi – Business Card</title>
<link rel="stylesheet" href="https://fonts.googleapis.com/css2?family=Arimo:wght@400;700&display=swap">
<style>
  :root {
    --page-bg: #2b2b2b;
    --card-white: #ffffff;
    --card-dark: #2a2728;
    --ink: #1f1f1f;
    --leaf-green: #2fb24a;
    --soft-pink: #e97dbf;
    --contact-text: #f2f2f2;
    --mark-grey: #8a8a8a;
  }
  * { margin: 0; padding: 0; box-sizing: border-box; }
  html, body {
    width: 1200px; height: 900px; overflow: hidden;
    background: var(--page-bg);
    font-family: "Arimo", Arial, sans-serif;
  }
  .card {
    position: absolute; left: 100px; top: 165px;
    width: 1000px; height: 570px;
    background: var(--card-white);
    overflow: hidden;
  }
  .card-bands { position: absolute; inset: 0; }
  .brand-seal {
    position: absolute; left: 55px; top: 88px;
    width: 120px; height: 120px; border-radius: 50%;
    border: 3px solid #c9c9c9;
    display: flex; align-items: center; justify-content: center;
    color: var(--leaf-green); font-weight: 700; font-size: 20px;
  }
  .title-rule {
    position: absolute; left: 205px; top: 80px;
    width: 10px; height: 125px;
    border-left: 3px solid var(--ink); border-right: 3px solid var(--ink);
  }
  .business-name {
    position: absolute; left: 235px; top: 88px;
    font-size: 54px; font-weight: 700; color: var(--ink);
    letter-spacing: 1px; white-space: nowrap; line-height: 1.1;
  }
  .tagline {
    position: absolute; left: 237px; top: 155px;
    font-size: 30px; font-weight: 700; color: var(--leaf-green);
    letter-spacing: 0.5px; white-space: nowrap;
  }
  .leader-name {
    position: absolute; left: 85px; top: 255px;
    font-size: 32px; font-weight: 700; color: var(--leaf-green);
    letter-spacing: 0.5px; line-height: 1.1;
  }
  .leader-role {
    position: absolute; left: 85px; top: 296px;
    font-size: 24px; color: var(--ink); line-height: 1.1;
  }
  .corner-mark {
    position: absolute; right: 60px; top: 270px;
    font-size: 40px; font-weight: 700; color: var(--mark-grey);
  }
  .contact-list {
    position: absolute; left: 85px; top: 455px;
    list-style: none; color: var(--contact-text);
    font-size: 27px; letter-spacing: 2px;
  }
  .contact-list li { display: flex; align-items: center; gap: 22px; height: 40px; }
  .contact-icon { width: 24px; height: 24px; }
</style>
</head>
<body>
  <div class="card">
    <svg class="card-bands" width="1000" height="570" viewBox="0 0 1000 570">
      <path d="M0,430 Q520,390 1000,150 L1000,570 L0,570 Z" fill="var(--card-dark)"/>
      <path d="M0,424 Q520,384 1000,144" fill="none" stroke="var(--leaf-green)" stroke-width="11"/>
      <path d="M0,400 Q520,360 1000,120" fill="none" stroke="var(--soft-pink)" stroke-width="12"/>
    </svg>

    <div class="brand-seal">Wexmoor</div>
    <div class="title-rule"></div>
    <h1 class="business-name">WEXMOOR TAI CHI</h1>
    <p class="tagline">Fitness, Health &amp; Relaxation</p>

    <h2 class="leader-name">BRANNA HOLT</h2>
    <p class="leader-role">Certificated Leader</p>

    <div class="corner-mark">Wexmoor</div>

    <ul class="contact-list">
      <li>
        <svg class="contact-icon" viewBox="0 0 24 24" aria-hidden="true">
          <rect x="1" y="1" width="22" height="22" rx="4" fill="none" stroke="#f2f2f2" stroke-width="2"/>
          <path d="M8 6c-1 1-1 3 1 6s4 5 6 5l1.5-1.5-2.5-2-1.2 1c-1-.5-2.5-2-3-3l1-1.2-2-2.5z" fill="#f2f2f2"/>
        </svg>
        <span>4091 5528</span>
      </li>
      <li>
        <svg class="contact-icon" viewBox="0 0 24 24" aria-hidden="true">
          <rect x="1" y="1" width="22" height="22" rx="4" fill="none" stroke="#f2f2f2" stroke-width="2"/>
          <rect x="5" y="7" width="14" height="10" fill="none" stroke="#f2f2f2" stroke-width="1.6"/>
          <path d="M5 7l7 6 7-6" fill="none" stroke="#f2f2f2" stroke-width="1.6"/>
        </svg>
        <span>hello@wexmoortaichi.com</span>
      </li>
    </ul>
  </div>
</body>
</html>
```